Mediation Website Design Upgrade

Project Details: https://files.plumvaro.net/sheet/k/8Wd3mPzqTuLhXe7nRaBo4_KcVy-92jsQ2fLgNwHd/view?ref=shared

Number of Pages Required

2 page

Font styles to use
Sans Serif

```html
<!DOCTYPE html>
<html lang="en">
<head>
<meta charset="utf-8">
<title>Mediation Services – Harborline Mediation Group</title>
<link rel="stylesheet" href="https://fonts.googleapis.com/css2?family=Nunito+Sans:wght@400;600;700;800&display=swap">
<style>
  :root {
    --ink: #1b1b1b;
    --text: #555a5e;
    --teal: #3f6b67;
    --green: #5f9a3a;
    --green-dark: #3e6f63;
    --green-light: #78a82f;
    --panel: #f2f2f2;
    --white: #ffffff;
    --hero-slate: #5c6b78;
  }
  * { box-sizing: border-box; margin: 0; padding: 0; }
  html, body { width: 1200px; height: 2318px; overflow: hidden; }
  body { font-family: "Nunito Sans", sans-serif; color: var(--ink); background: var(--white); position: relative; }
  ul { list-style: none; }

  .site-header { height: 100px; display: flex; align-items: center; padding: 0 45px 0 98px; justify-content: space-between; }
  .brand { display: flex; align-items: center; gap: 10px; }
  .brand-dot { width: 38px; height: 38px; border-radius: 50%; background: var(--teal); }
  .brand-name { font-size: 19px; font-weight: 800; line-height: 1.05; color: var(--ink); width: 190px; }
  .main-nav { display: flex; gap: 31px; font-size: 17px; }
  .main-nav a { color: var(--ink); text-decoration: none; }
  .main-nav a.active { font-weight: 700; }

  .hero { position: relative; height: 422px; background: linear-gradient(90deg, #5f6d7a 0%, #6e7c88 25%, #a79c92 55%, #c9b9aa 75%, #d9d4ce 100%); }
  .hero-title { position: absolute; left: 122px; top: 160px; color: var(--white); font-size: 52px; font-weight: 800; line-height: 48px; letter-spacing: 0.5px; }

  .intro { height: 480px; text-align: center; padding-top: 62px; }
  .intro h2 { font-size: 32px; font-weight: 800; line-height: 38px; }
  .intro h3 { font-size: 26px; font-weight: 800; line-height: 38px; }
  .rule { width: 48px; height: 3px; background: var(--teal); margin: 12px auto 26px; }
  .intro p { width: 930px; margin: 0 auto 14px; font-size: 14.5px; line-height: 23px; color: var(--text); }

  .focus { display: flex; height: 570px; }
  .focus-copy { width: 615px; background: var(--panel); padding: 118px 0 0 110px; }
  .focus-copy h2 { font-size: 30px; font-weight: 800; }
  .focus-copy .rule { margin: 12px 0 30px 2px; width: 52px; }
  .focus-list li { position: relative; padding-left: 22px; font-size: 15.5px; color: var(--text); line-height: 24px; margin-bottom: 14px; max-width: 420px; }
  .focus-list svg { position: absolute; left: 0; top: 6px; }
  .focus-photo { flex: 1; background: linear-gradient(160deg, #c9c7c2 0%, #8f8c86 45%, #5b5955 75%, #e6e6e4 100%); }

  .tasks { position: relative; height: 521px; background: linear-gradient(100deg, #3f6f64 0%, #5b8f4a 50%, #6fa030 100%); color: var(--white); text-align: center; padding-top: 78px; }
  .tasks h2 { font-size: 29px; font-weight: 700; line-height: 40px; }
  .tasks .rule { background: var(--white); margin: 10px auto 62px; }
  .task-cols { display: flex; text-align: left; padding-left: 105px; gap: 48px; }
  .task-cols ul { width: 485px; }
  .task-cols li { position: relative; padding-left: 25px; font-size: 15.5px; line-height: 24px; margin-bottom: 15px; }
  .task-cols svg { position: absolute; left: 0; top: 5px; }

  .site-footer { height: 225px; text-align: center; padding-top: 22px; }
  .footer-brand { display: inline-flex; align-items: center; gap: 8px; font-size: 17px; font-weight: 800; }
  .footer-brand span.dot { width: 20px; height: 20px; border-radius: 50%; background: var(--teal); }
  .footer-nav { display: flex; justify-content: center; gap: 31px; font-size: 17px; margin-top: 28px; }
  .footer-nav a { color: var(--ink); text-decoration: none; }
  .copyright { font-size: 14px; color: #444; margin-top: 14px; }
  .social { display: flex; justify-content: center; gap: 4px; margin-top: 12px; }
  .social span { width: 40px; height: 40px; border: 2px solid var(--green); border-radius: 50%; }
</style>
</head>
<body>
  <header class="site-header">
    <div class="brand">
      <span class="brand-dot"></span>
      <span class="brand-name">Harborline Mediation Group</span>
    </div>
    <nav class="main-nav">
      <a href="#">Home</a>
      <a href="#" class="active">Mediation Services</a>
      <a href="#">Conflict Consulting</a>
      <a href="#">Negotiation</a>
      <a href="#">About Us</a>
      <a href="#">Blog</a>
      <a href="#">Contact</a>
    </nav>
  </header>

  <section class="hero" role="img" aria-label="Photo of a frustrated couple sitting apart on a sofa">
    <h1 class="hero-title">MEDIATION<br>SERVICES</h1>
  </section>

  <section class="intro">
    <h2>MEDIATION SERVICES</h2>
    <h3>OUR PRIMARY FOCUS</h3>
    <div class="rule"></div>
    <p>HMG offers decades of conflict resolution experience in such diverse settings as community meetings, non-profit boards, courts, corporate boardrooms, family living rooms and kitchen tables. Firm principal Marian Okafor has worked for over 30 years in various business, family and organizational settings including finance, insurance, technology, restaurants, family businesses and many nonprofits. These nonprofits include community foundations, higher education, art cooperatives and religious communities.</p>
    <p>In addition to formal training and business experience, Marian’s life has uniquely prepared her for a career in mediation. She grew up in a large extended family, is now part of a blended family, and has worked through inter-generational and family business issues throughout her life.</p>
    <p>Based on Marian’s experience, education, and passion, her firm specializes in selected area of the growing conflict resolution field.</p>
  </section>

  <section class="focus">
    <div class="focus-copy">
      <h2>KEY AREAS OF FOCUS INCLUDE</h2>
      <div class="rule"></div>
      <ul class="focus-list">
        <li><svg width="10" height="14" viewBox="0 0 10 14"><path d="M2 1l6 6-6 6" fill="none" stroke="#5f9a3a" stroke-width="3"/></svg>Conflict Coaching</li>
        <li><svg width="10" height="14" viewBox="0 0 10 14"><path d="M2 1l6 6-6 6" fill="none" stroke="#5f9a3a" stroke-width="3"/></svg>Adult-Sibling and Elder Mediation</li>
        <li><svg width="10" height="14" viewBox="0 0 10 14"><path d="M2 1l6 6-6 6" fill="none" stroke="#5f9a3a" stroke-width="3"/></svg>Commercial Mediation – within the same organization or between different organizations</li>
        <li><svg width="10" height="14" viewBox="0 0 10 14"><path d="M2 1l6 6-6 6" fill="none" stroke="#5f9a3a" stroke-width="3"/></svg>Nonprofit Mediation</li>
        <li><svg width="10" height="14" viewBox="0 0 10 14"><path d="M2 1l6 6-6 6" fill="none" stroke="#5f9a3a" stroke-width="3"/></svg>Facilitation of meetings and processes</li>
        <li><svg width="10" height="14" viewBox="0 0 10 14"><path d="M2 1l6 6-6 6" fill="none" stroke="#5f9a3a" stroke-width="3"/></svg>Negotiation – coaching or as</li>
      </ul>
    </div>
    <div class="focus-photo" role="img" aria-label="Photo of a man gesturing in frustration beside a woman with crossed arms at a table"></div>
  </section>

  <section class="tasks" role="img" aria-label="Green-tinted photo of hands over a desk with documents, behind the task list">
    <h2>WORKING WITH A PROFESSIONAL, MEDIATION CAN PERFORM<br>ANY OF THE FOLLOWING TASKS AND MORE</h2>
    <div class="rule"></div>
    <div class="task-cols">
      <ul>
        <li><svg width="18" height="14" viewBox="0 0 18 14"><path d="M1 7l5 5L17 1" fill="none" stroke="#fff" stroke-width="3"/></svg>Organize discussions for thorough and timely consideration</li>
        <li><svg width="18" height="14" viewBox="0 0 18 14"><path d="M1 7l5 5L17 1" fill="none" stroke="#fff" stroke-width="3"/></svg>Work to provide safe discussions while promoting candidness and honesty</li>
        <li><svg width="18" height="14" viewBox="0 0 18 14"><path d="M1 7l5 5L17 1" fill="none" stroke="#fff" stroke-width="3"/></svg>Enlist objective subject matter experts to ensure that pertinent and accurate information is available for decision making</li>
        <li><svg width="18" height="14" viewBox="0 0 18 14"><path d="M1 7l5 5L17 1" fill="none" stroke="#fff" stroke-width="3"/></svg>Ensure that all viewpoints and perspectives are heard and considered</li>
      </ul>
      <ul>
        <li><svg width="18" height="14" viewBox="0 0 18 14"><path d="M1 7l5 5L17 1" fill="none" stroke="#fff" stroke-width="3"/></svg>Develop a process by which the situation is explored and viable alternatives are identified</li>
        <li><svg width="18" height="14" viewBox="0 0 18 14"><path d="M1 7l5 5L17 1" fill="none" stroke="#fff" stroke-width="3"/></svg>Establish criteria by which forward progress occurs</li>
        <li><svg width="18" height="14" viewBox="0 0 18 14"><path d="M1 7l5 5L17 1" fill="none" stroke="#fff" stroke-width="3"/></svg>Oversee delicate or difficult decision making</li>
        <li><svg width="18" height="14" viewBox="0 0 18 14"><path d="M1 7l5 5L17 1" fill="none" stroke="#fff" stroke-width="3"/></svg>Document outcomes, plans, and responsibilities</li>
        <li><svg width="18" height="14" viewBox="0 0 18 14"><path d="M1 7l5 5L17 1" fill="none" stroke="#fff" stroke-width="3"/></svg>Provide counsel and guidance for implementing new plans</li>
      </ul>
    </div>
  </section>

  <footer class="site-footer">
    <div class="footer-brand"><span class="dot"></span>Harborline Mediation Group</div>
    <nav class="footer-nav">
      <a href="#">Home</a>
      <a href="#">Mediation Services</a>
      <a href="#">Conflict Consulting</a>
      <a href="#">Negotiation</a>
      <a href="#">About Us</a>
      <a href="#">Blog</a>
      <a href="#">Contact</a>
    </nav>
    <p class="copyright">© 2020 Company Name | All Rights Reserved</p>
    <div class="social" aria-label="Social links">
      <span></span><span></span><span></span><span></span>
    </div>
  </footer>
</body>
</html>
```